Carpentry and Building Business Card

I'm looking for a business card that is minimalistic and that incorporates the theme of my Velmor logo.
On one side I'd like the VELMOR logo with my details on the other side.
Double sided with curved edges

Target Market(s)

Construction / renovation
Adults

Industry/Entity Type

Tradesman

Contact Information for Business Card

Logo on one side, details on the other

Colors

Designer to choose only greyscale colors for use in the design.

Requirements
Must have
• Nilo Petrakis
VELMOR CONSTRUCT
Carpentry & Building Services
0481236574
Velmorconstruct@brixmail.com
Lic No. 718263D
Nice to have
• Fb and insta icons. @velmorconstruct
Should not have
• No hammer or tool icons please.

No address line.

```html
<!DOCTYPE html>
<html lang="en">
<head>
<meta charset="utf-8">
<title>Velmor Business Card</title>
<link href="https://fonts.googleapis.com/css2?family=Montserrat:wght@500;600&family=Arimo:wght@400&display=swap" rel="stylesheet">
<style>
  :root {
    --backdrop: #a9a9a9;
    --card: #221f20;
    --accent: #f0983a;
    --ink: #e9e9e9;
    --rule: #9a9a9a;
  }
  * { margin: 0; padding: 0; box-sizing: border-box; }
  html, body { width: 1200px; height: 1200px; overflow: hidden; }
  body { background: var(--backdrop); position: relative; font-family: "Arimo", Arial, sans-serif; }
  .card {
    position: absolute; top: 305px; width: 368px; height: 594px;
    background: var(--card); border-radius: 20px;
  }
  .card--front { left: 202px; }
  .card--back { left: 600px; }
  .brand {
    position: absolute; left: 0; right: 0;
    display: flex; align-items: center; justify-content: center; gap: 16px;
  }
  .brand__mark { width: 52px; height: 52px; border: 2px solid var(--accent); }
  .brand__name {
    font-family: "Montserrat", sans-serif; font-weight: 500;
    font-size: 34px; letter-spacing: 10px; color: var(--ink);
  }
  .card--front .brand { top: 285px; }
  .card--back .brand { top: 140px; }
  .social {
    position: absolute; left: 0; right: 0; top: 526px;
    display: flex; align-items: center; justify-content: center; gap: 8px;
    color: var(--ink); font-size: 17px;
  }
  .social__mark { width: 20px; height: 20px; background: var(--accent); border-radius: 4px; }
  .details { position: absolute; left: 0; right: 0; top: 364px; text-align: center; color: var(--ink); }
  .details__name {
    font-family: "Montserrat", sans-serif; font-weight: 600;
    font-size: 21px; color: var(--accent); letter-spacing: -0.3px; line-height: 24px;
  }
  .details__role { font-size: 16px; margin-top: 3px; letter-spacing: 0.3px; }
  .details__rule { width: 92px; height: 1px; background: var(--rule); margin: 16px auto 14px; }
  .details__phone { font-size: 20px; }
  .details__email { font-size: 16px; margin-top: 6px; }
  .details__licence { font-size: 16px; }
  .details__licence span { color: var(--accent); }
</style>
</head>
<body>
  <section class="card card--front">
    <div class="brand">
      <div class="brand__mark"></div>
      <div class="brand__name">VELMOR.</div>
    </div>
    <div class="social">
      <div class="social__mark"></div>
      <span>@velmorconstruct</span>
    </div>
  </section>

  <section class="card card--back">
    <div class="brand">
      <div class="brand__mark"></div>
      <div class="brand__name">VELMOR.</div>
    </div>
    <div class="details">
      <p class="details__name">NILO PETRAKIS</p>
      <p class="details__role">CARPENTRY &amp; BUILDING</p>
      <div class="details__rule"></div>
      <p class="details__phone">0481236574</p>
      <p class="details__email">VELMORCONSTRUCT@BRIXMAIL.COM</p>
      <div class="details__rule"></div>
      <p class="details__licence"><span>LIC NO.</span> 718263D</p>
    </div>
  </section>
</body>
</html>
```